Business Cards for a small business advisory (business services)

Professional look. Same as would apply for a lawyer, accountant, or other financial services professional. Please use the logo colors

Target Market(s)

small business owners

Industry/Entity Type

Financial Servics

Contact Information for Business Card

Name: Glenn R. Whitaker, CAIA / Title: Business Advisor / Office #: (555) 284-7193 / Mobile #: (555) 903-6418 / Email: g.whitaker@ambervalebusinessbrokers.example / Web: www.ambervalebusinessbrokers.example

Font styles to use
Sans Serif

```html
<!DOCTYPE html>
<html lang="en">
<head>
<meta charset="utf-8">
<title>Ambervale Business Brokers &amp; Advisors — Business Cards</title>
<link rel="stylesheet" href="https://fonts.googleapis.com/css2?family=Montserrat:wght@500;600;700&family=Roboto:wght@400;500&display=swap">
<style>
  :root {
    --backdrop: #a9a9a9;
    --card-navy: #1f4380;
    --card-navy-deep: #1a3a6f;
    --accent-green: #8dc63f;
    --ink-white: #ffffff;
  }
  * { box-sizing: border-box; margin: 0; padding: 0; }
  html, body {
    width: 1200px;
    height: 1015px;
    overflow: hidden;
    background: var(--backdrop);
  }
  .sheet {
    position: relative;
    width: 1200px;
    height: 1015px;
  }
  .card {
    position: absolute;
    width: 620px;
    height: 354px;
    background: radial-gradient(ellipse at 35% 30%, var(--card-navy) 0%, var(--card-navy-deep) 100%);
    border-bottom: 9px solid var(--accent-green);
    box-shadow: 0 6px 14px rgba(0,0,0,0.28);
    color: var(--ink-white);
    overflow: hidden;
  }
  .card--front { left: 70px; top: 80px; }
  .card--back  { left: 510px; top: 560px; }

  /* Front */
  .brand {
    position: absolute;
    left: 96px;
    top: 112px;
  }
  .brand__row {
    display: flex;
    align-items: center;
    gap: 18px;
  }
  .brand__dot {
    width: 52px;
    height: 52px;
    border-radius: 50%;
    background: var(--ink-white);
    flex: none;
  }
  .brand__name {
    font-family: "Montserrat", sans-serif;
    font-weight: 700;
    font-size: 64px;
    line-height: 1;
    letter-spacing: 0.5px;
    color: var(--ink-white);
  }
  .brand__descriptor {
    margin: 10px 0 0 70px;
    font-family: "Montserrat", sans-serif;
    font-weight: 600;
    font-size: 19px;
    letter-spacing: 2.4px;
    text-transform: uppercase;
    color: var(--accent-green);
  }
  .brand__tagline {
    margin: 5px 0 0 70px;
    font-family: "Montserrat", sans-serif;
    font-weight: 500;
    font-size: 10.5px;
    letter-spacing: 1.1px;
    text-transform: uppercase;
    color: var(--ink-white);
  }

  /* Back */
  .person {
    position: absolute;
    left: 36px;
    top: 74px;
  }
  .person__name {
    font-family: "Montserrat", sans-serif;
    font-weight: 700;
    font-size: 25px;
    letter-spacing: 0.6px;
    text-transform: uppercase;
    color: var(--accent-green);
  }
  .person__title {
    margin-top: 2px;
    font-family: "Roboto", sans-serif;
    font-weight: 400;
    font-size: 18px;
    color: var(--ink-white);
  }
  .contact {
    position: absolute;
    left: 36px;
    bottom: 26px;
    list-style: none;
    font-family: "Roboto", sans-serif;
    font-size: 17px;
    line-height: 1.45;
  }
  .contact__item {
    display: flex;
    align-items: center;
    gap: 10px;
  }
  .contact__icon {
    width: 18px;
    height: 18px;
    flex: none;
    stroke: var(--accent-green);
    fill: none;
    stroke-width: 2;
    stroke-linecap: round;
    stroke-linejoin: round;
  }
  .contact__highlight { color: var(--accent-green); }
  .brand-mark-area {
    position: absolute;
    right: 60px;
    top: 40px;
    width: 200px;
    height: 200px;
    border-radius: 50%;
    background: rgba(255,255,255,0.12);
  }
</style>
</head>
<body>
<main class="sheet">

  <section class="card card--front" aria-label="Business card front">
    <div class="brand">
      <div class="brand__row">
        <span class="brand__dot" aria-hidden="true"></span>
        <span class="brand__name">Ambervale</span>
      </div>
      <p class="brand__descriptor">Business Brokers &amp; Advisors</p>
      <p class="brand__tagline">Your guide to confidently buy or sell a local business today</p>
    </div>
  </section>

  <section class="card card--back" aria-label="Business card back">
    <div class="person">
      <h1 class="person__name">Glenn R. Whitaker, CAIA</h1>
      <p class="person__title">Business Advisor</p>
    </div>

    <div class="brand-mark-area" role="img" aria-label="Brand emblem area"></div>

    <ul class="contact">
      <li class="contact__item">
        <svg class="contact__icon" viewBox="0 0 24 24" aria-hidden="true"><path d="M5 3h4l2 5-2.5 1.5a11 11 0 0 0 6 6L16 13l5 2v4a2 2 0 0 1-2 2A16 16 0 0 1 3 5a2 2 0 0 1 2-2z"/></svg>
        <span>(555) 284-7193</span>
      </li>
      <li class="contact__item">
        <svg class="contact__icon" viewBox="0 0 24 24" aria-hidden="true"><rect x="6" y="2" width="12" height="20" rx="2"/><line x1="11" y1="18" x2="13" y2="18"/></svg>
        <span>(555) 903-6418</span>
      </li>
      <li class="contact__item">
        <svg class="contact__icon" viewBox="0 0 24 24" aria-hidden="true"><rect x="2" y="5" width="20" height="14" rx="1"/><polyline points="2,5 12,13 22,5"/></svg>
        <span>g.whitaker@ambervalebusinessbrokers.example</span>
      </li>
      <li class="contact__item">
        <svg class="contact__icon" viewBox="0 0 24 24" aria-hidden="true"><circle cx="12" cy="12" r="10"/><line x1="2" y1="12" x2="22" y2="12"/><ellipse cx="12" cy="12" rx="4" ry="10"/></svg>
        <span>www.<span class="contact__highlight">ambervalebusinessbrokers</span>.example</span>
      </li>
    </ul>
  </section>

</main>
</body>
</html>
```